We need a Glass-Shattering Brochure

We area start up renewable company based in the UK but operate in West Africa. We have a unique blend of local know-how and international exposure to latest solar technology. We pride ourselves in bringing next generation, ground breaking, value for money solar products to Africa.

We are launching a massive campaign to introduce some of the world's best solar product to our high net-worth clients and decision makers. This will be a single brochure of A4 size on 8 pages. Details of the page content is attached.

Also a sample of what we like is attached. The brochure must be clean , fresh, very contemporary and straight to the point - Clear

I have attached a link to some of our installation pictures and some pictures that I think you might need. But feel free to source pictures you think will be appropriate for the intended audience.

You can access some of our paid pictures and installation pictures here https://filedrop-example.net/f/x7KpQm2RtLw9ZvNc4HdYs8BjE

Apologies to everyone. We have just uploaded the brochure content

Target Market(s)

Top company executives

Industry/Entity Type

It Company

Requirements
Must have
• Similar font used in the sample brochure attached. White background. Hint of the green. Please check out our website at www.tolvarpower.co.uk
Nice to have
• Other pictures other than the ones provided

```html
<!DOCTYPE html>
<html lang="en">
<head>
<meta charset="utf-8">
<title>Tolvar Power Brochure – Savings, KPI, Contact</title>
<link rel="stylesheet" href="https://fonts.googleapis.com/css2?family=Nunito+Sans:wght@300;400&display=swap">
<style>
  :root {
    --canvas-bg: #ece8e1;
    --page-white: #ffffff;
    --gutter-grey: #d9d9d9;
    --heading-grey: #5a5a5a;
    --body-grey: #3f3f3f;
    --chart-green: #a8cf45;
    --chart-blue: #8fb3d9;
    --chart-orange: #f07d1a;
    --chart-teal: #2e9aa8;
    --chart-line: #4a6fb5;
    --photo-light: #eef0f1;
    --photo-mid: #b9bcbd;
    --photo-floor: #8a705a;
    --on-photo: #ffffff;
  }
  * { box-sizing: border-box; margin: 0; padding: 0; }
  html, body { width: 1200px; height: 1200px; overflow: hidden; }
  body {
    background: var(--canvas-bg);
    font-family: "Nunito Sans", sans-serif;
    font-weight: 300;
    position: relative;
  }
  .spread {
    position: absolute;
    left: 60px; top: 218px;
    width: 1080px; height: 764px;
    display: flex;
    box-shadow: 0 6px 18px rgba(0,0,0,0.18);
  }
  .page-left {
    position: relative;
    width: 540px; height: 100%;
    background: linear-gradient(90deg, var(--page-white) 0%, var(--page-white) 68%, var(--gutter-grey) 100%);
  }
  .column {
    position: absolute;
    top: 38px;
    width: 147px;
  }
  .col-savings { left: 37px; }
  .col-kpi { left: 197px; }
  .col-advantage { left: 356px; }
  .column-title {
    font-weight: 300;
    font-size: 21px;
    line-height: 26px;
    color: var(--heading-grey);
    height: 52px;
    display: flex;
    align-items: flex-end;
    letter-spacing: 0.3px;
  }
  .chart {
    display: block;
    margin-top: 13px;
    width: 138px;
  }
  .column-body {
    position: absolute;
    top: 195px;
    left: 0;
    width: 147px;
  }
  .column-body p {
    font-size: 10.2px;
    line-height: 13.1px;
    color: var(--body-grey);
    margin-bottom: 13px;
  }
  .page-right {
    position: relative;
    width: 540px; height: 100%;
  }
  .photo {
    position: absolute; inset: 0;
    background:
      linear-gradient(180deg, rgba(0,0,0,0) 0%, rgba(0,0,0,0) 58%, var(--photo-floor) 100%),
      linear-gradient(100deg, var(--photo-mid) 0%, var(--photo-light) 45%, #c9ced2 75%, var(--photo-light) 100%);
  }
  .contact {
    position: absolute;
    left: 38px; top: 60px;
    width: 190px;
    color: var(--on-photo);
  }
  .contact-title {
    font-weight: 400;
    font-size: 21px;
    line-height: 26px;
    margin-bottom: 13px;
  }
  .contact p {
    font-size: 10.2px;
    line-height: 13px;
    margin-bottom: 13px;
  }
</style>
</head>
<body>
<main class="spread">
  <section class="page-left">
    <article class="column col-savings">
      <h2 class="column-title">Your<br>Savings Live</h2>
      <svg class="chart" viewBox="0 0 138 90" aria-label="Energy generated vs used chart">
        <rect x="0.5" y="0.5" width="137" height="89" fill="#fff" stroke="#bbb"/>
        <text x="69" y="7" font-size="4" text-anchor="middle" fill="#333" font-family="sans-serif">Energy Generated Vs Used</text>
        <g stroke="#eee" stroke-width="0.5">
          <line x1="12" y1="15" x2="100" y2="15"/><line x1="12" y1="30" x2="100" y2="30"/>
          <line x1="12" y1="45" x2="100" y2="45"/><line x1="12" y1="60" x2="100" y2="60"/>
          <line x1="12" y1="75" x2="100" y2="75"/>
        </g>
        <g fill="var(--chart-green)">
          <rect x="22" y="28" width="2" height="49"/><rect x="36" y="28" width="2" height="49"/>
          <rect x="50" y="28" width="2" height="49"/><rect x="64" y="28" width="2" height="49"/>
          <rect x="78" y="28" width="2" height="49"/><rect x="92" y="32" width="2" height="45"/>
        </g>
        <g fill="var(--chart-orange)">
          <rect x="18" y="70" width="2" height="7"/><rect x="32" y="72" width="2" height="5"/>
          <rect x="46" y="71" width="2" height="6"/><rect x="60" y="72" width="2" height="5"/>
          <rect x="74" y="71" width="2" height="6"/><rect x="88" y="72" width="2" height="5"/>
        </g>
        <g fill="#e58ab0">
          <rect x="26" y="73" width="2" height="4"/><rect x="40" y="73" width="2" height="4"/>
          <rect x="54" y="73" width="2" height="4"/><rect x="68" y="73" width="2" height="4"/>
          <rect x="82" y="73" width="2" height="4"/>
        </g>
        <polyline points="16,32 30,30 44,31 58,30 72,31 86,33 98,33" fill="none" stroke="#9ab" stroke-width="0.8"/>
        <line x1="12" y1="77" x2="100" y2="77" stroke="#999" stroke-width="0.5"/>
        <g font-size="2.8" fill="#555" font-family="sans-serif">
          <rect x="104" y="17" width="3" height="2" fill="var(--chart-blue)"/><text x="108" y="19">Energy Used</text>
          <rect x="104" y="21" width="3" height="2" fill="var(--chart-green)"/><text x="108" y="23">Solar</text>
          <rect x="104" y="25" width="3" height="2" fill="var(--chart-orange)"/><text x="108" y="27">Gen</text>
          <rect x="104" y="29" width="3" height="2" fill="#e58ab0"/><text x="108" y="31">Grid</text>
        </g>
      </svg>
      <div class="column-body">
        <p>This is where we separate the boys from the men. All our existing solar system in Africa are all connected via the Internet to our central cloud database. The online customer dashboard was designed In-house by the Tolvar Power Technical Team. This unique opportunity gives us the edge to monitor the performance of each plant remotely and compare results with predicted forecast. We can monitor and activate early fault detection, mitigate downtime risk and schedule offsite maintenance.</p>
        <p>It's another first from Tolvar Power. since the 9th of Feb 2014, we have publicly made available a sample of our solar system. Its an exemplary outstanding feature that continuously separate us from competition.</p>
      </div>
    </article>

    <article class="column col-kpi">
      <h2 class="column-title">Your KPI</h2>
      <svg class="chart" viewBox="0 0 138 62" aria-label="Savings in Naira chart">
        <rect x="0.5" y="0.5" width="137" height="61" fill="#fff" stroke="#bbb"/>
        <text x="69" y="7" font-size="4" text-anchor="middle" fill="#333" font-family="sans-serif">Savings In Naira</text>
        <g font-size="3" fill="#555" font-family="sans-serif">
          <text x="6" y="14">2,000,000</text><text x="6" y="32">1,000,000</text><text x="20" y="50">0</text>
        </g>
        <rect x="30" y="19" width="14" height="30" fill="var(--chart-blue)"/>
        <rect x="45" y="40" width="14" height="9" fill="var(--chart-orange)"/>
        <rect x="78" y="19" width="14" height="30" fill="var(--chart-blue)"/>
        <rect x="93" y="40" width="14" height="9" fill="var(--chart-orange)"/>
        <line x1="24" y1="49" x2="122" y2="49" stroke="#999" stroke-width="0.5"/>
        <g font-size="3" fill="#555" font-family="sans-serif">
          <text x="38" y="54">2014-2015</text><text x="86" y="54">2015-2016</text>
          <text x="110" y="58">Financial Year</text>
          <rect x="120" y="12" width="3" height="3" fill="var(--chart-blue)"/><text x="124" y="15">Gen</text>
          <rect x="120" y="17" width="3" height="3" fill="var(--chart-orange)"/><text x="124" y="20">Grid</text>
        </g>
      </svg>
      <div class="column-body">
        <p>Every TPX account will have their dedicated permanence dashboard, where they can monitor their savings in near real time. Every important Key Performance Indicator (KPI) is available online from, savings in local currency, savings in diesel, Year to Date Savings in diesel, Energy Generated to Energy Used. TPX clients will have the option to track the economic impact of the product on a monthly basis.</p>
        <p>This will continuously allow to improve services to our customer and help deliver unbeatable value added service.</p>
      </div>
    </article>

    <article class="column col-advantage">
      <h2 class="column-title">Advantage,<br>You !</h2>
      <svg class="chart" viewBox="0 0 138 110" aria-label="Plant output vs forecast chart">
        <rect x="0" y="0" width="138" height="5" fill="#e4e4e4"/>
        <text x="3" y="4" font-size="3" fill="#333" font-family="sans-serif">Plant Output vs Forecast</text>
        <rect x="6" y="9" width="126" height="96" fill="#fff" stroke="#ccc" stroke-width="0.5"/>
        <rect x="14" y="13" width="110" height="83" fill="#fff" stroke="#ccc" stroke-width="0.5"/>
        <g fill="var(--chart-teal)">
          <rect x="16" y="60" width="4" height="36"/><rect x="21" y="67" width="4" height="29"/>
          <rect x="26" y="70" width="4" height="26"/><rect x="31" y="74" width="4" height="22"/>
          <rect x="36" y="72" width="4" height="24"/><rect x="41" y="75" width="4" height="21"/>
          <rect x="46" y="78" width="4" height="18"/><rect x="51" y="80" width="4" height="16"/>
          <rect x="56" y="82" width="4" height="14"/><rect x="61" y="84" width="4" height="12"/>
          <rect x="78" y="52" width="4" height="44"/><rect x="83" y="40" width="4" height="56"/>
          <rect x="88" y="27" width="4" height="69"/><rect x="93" y="20" width="4" height="76"/>
          <rect x="98" y="22" width="4" height="74"/><rect x="103" y="21" width="4" height="75"/>
          <rect x="108" y="25" width="4" height="71"/>
        </g>
        <polyline points="16,94 50,93 62,90 70,60 74,30 78,22 84,40 92,70 100,88 120,94" fill="none" stroke="var(--chart-line)" stroke-width="0.8"/>
        <g font-size="2.6" fill="#555" font-family="sans-serif">
          <rect x="16" y="100" width="3" height="2" fill="var(--chart-line)"/><text x="20" y="102">Output</text>
          <rect x="90" y="100" width="3" height="2" fill="var(--chart-teal)"/><text x="94" y="102">Forecast</text>
        </g>
      </svg>
      <div class="column-body">
        <p>All our inverters are fitted with Fault Detection Alert Systems. Which send us an email in real time the moment a fault incident is logged</p>
        <p>Before installation, each unit is simulated against the worse case scenario parameters. In other words, we have a forecast of what and how your system will perform for the next 25 years. A performance alert is easily raised whenever your actual online performance falls below our predicted forecast.</p>
        <p>Seeing is believing. With the online Dashboard, customers can see exactly how much they are saving in monetary terms. The dashboard has several KPIs like Year to Date Savings on Diesel, Year To Date Savings in Local Currency, How Much Power Generated by the Solar System, How Much Power Used overall. Infact, our client can compare how much power received from Grid, Gen and Solar.</p>
      </div>
    </article>
  </section>

  <section class="page-right">
    <div class="photo" role="img" aria-label="Sunlit glass corridor with solar panel facade, inverters mounted on the wall and patterned light on a wooden floor"></div>
    <div class="contact">
      <h2 class="contact-title">Contact Us</h2>
      <p>14 Harwell Crescent,<br>Chelmsford, Essex, United<br>Kingdom</p>
      <p>3rd Floor, Plot 12, Block 40,<br>Adeyemi Okafor Street,<br>Lekki, Lagos, Nigeria</p>
      <p>www.tolvarpower.co.uk</p>
    </div>
  </section>
</main>
</body>
</html>
```